SEO optimized website for Ko-Brava Corporate identity

I need an eye catching website (Flash splash is OK-I think) to help me promote my company of 10 years: Ko-Brava Inc. - we recently just awarded a design win for my logo design. See attached files.

The company name is Ko-Brava Inc. My current website is www.ko-brava-demo.ca and we specialize in large infrastructure - technology integration, both management and engineering. We have worked almost exclusively on VERD projects and wish to promote that.

I need it to be flexible enough for me to add pages for existing case studies and future case studies.

It is difficult to marry technology and green but do your best as I would like to highlight our VERD AP staff members.

The other side of my business is Small Medium Sized Business support and engineering. VOIP, Server, Desktop we have done it all.

My current site is www.ko-brava-demo.ca
Updates

Please use newly attached logo for designs.

All Please see some sample images to incorporate into the deisgns

Reason: Need more time to evaluate

Please use the correct/new logo in all designs

Please use the updated l;og that was included. Thank you.

Reason: I would like designers to modify their deisgns with the actual company logo. Only one design er has gotten it right. Please modify.

Reason: Still no time to devote to this. Sorry

Reason: Not ready to focus on it

Please only use the logo supplied int he source file zip

Target Market(s)

Both large infrstructure facility owners and small and medium sized businesses.

Industry/Entity Type

Business

Requirements
Must have
• SEO optimization
Easy for me to provide content going forward
Link to my FTP site
Links to my main partners
Separate login are for my clients to store files

```html
<!DOCTYPE html>
<html lang="en">
<head>
<meta charset="utf-8">
<title>Ko-Brava Inc. — Technology Infrastructure Specialists</title>
<link href="https://fonts.googleapis.com/css2?family=Ubuntu:wght@400;500;700&family=Arimo:wght@400;700&display=swap" rel="stylesheet">
<style>
:root{
  --orange:#ff6c00;
  --orange-light:#ff9a4a;
  --navy:#0f2f4a;
  --text:#555b61;
  --text-dark:#3f4448;
  --rule:#dcdee1;
  --bg-top:#ffffff;
  --bg-bottom:#ebecee;
  --divider:#1b1b1b;
}
*{box-sizing:border-box;margin:0;padding:0}
html,body{width:1200px;height:1140px;overflow:hidden}
body{
  position:relative;
  background:linear-gradient(180deg,var(--bg-top) 0,var(--bg-top) 130px,#f3f4f5 600px,var(--bg-bottom) 1140px);
  font-family:"Arimo",Arial,sans-serif;color:var(--text);
}
a{text-decoration:none;color:inherit}
ul{list-style:none}

/* Brand */
.brand{position:absolute;left:66px;top:50px;display:block}
.brand-name{font-family:"Ubuntu",sans-serif;font-size:52px;font-weight:400;color:var(--navy);line-height:1}

/* Utility bar */
.utility{position:absolute;left:674px;top:56px;width:490px;height:51px;border:1px solid #e3e4e6;border-radius:10px;background:#fff;display:flex;align-items:center;padding-left:20px}
.utility-links{display:flex;gap:10px;font-family:"Ubuntu",sans-serif;font-size:15px;color:var(--orange);font-weight:500}
.utility-links span.sep{color:var(--orange)}
.search{position:absolute;left:220px;top:9px;width:258px;height:32px;border:1px solid #e1e2e4;border-radius:3px;display:flex;align-items:center;justify-content:space-between;padding:0 12px 0 14px;font-family:"Ubuntu",sans-serif;font-size:15px;color:var(--text-dark);font-weight:500}

/* Main panel */
.panel{position:absolute;left:36px;top:164px;width:1128px;height:656px;border:1px solid #d9dadc;border-radius:9px;overflow:hidden;background:#eef0f2}
.nav{display:flex;height:60px;background:linear-gradient(180deg,#ffffff,#ededee);border-bottom:1px solid #d7d8da}
.nav a{display:flex;align-items:center;justify-content:center;font-family:"Ubuntu",sans-serif;font-size:19px;font-weight:500;color:var(--orange);border-right:1px solid #dcdddf;letter-spacing:.3px}
.nav a:last-child{border-right:0}
.nav a.is-active{background:linear-gradient(180deg,var(--orange-light),var(--orange));color:#fff}

.hero{position:absolute;left:0;top:60px;width:1128px;height:360px;background:linear-gradient(180deg,#c9d2da 0%,#b4bec8 40%,#7f8890 70%,#9ba4aa 100%)}
.hero-caption{position:absolute;left:521px;top:22px;width:565px;height:180px;background:rgba(255,255,255,.82);border-radius:4px;padding:10px 22px}
.hero-title{font-family:"Ubuntu",sans-serif;font-size:22.5px;font-weight:500;color:var(--orange);line-height:31px;letter-spacing:-.1px}
.hero-text{font-family:"Ubuntu",sans-serif;font-size:15px;font-weight:700;color:var(--text-dark);line-height:31px;margin-top:2px;padding-right:14px}
.slider-dots{position:absolute;left:817px;top:260px;display:flex;gap:14px}
.slider-dots span{width:34px;height:34px;border:3px solid var(--orange);background:#fff;border-radius:4px}
.slider-dots span.is-current{background:var(--orange);border-color:#fff;outline:1px solid var(--orange)}

.features{position:absolute;left:0;top:420px;width:1128px;height:236px;display:flex;background:linear-gradient(180deg,rgba(250,251,252,.9),#eef0f2)}
.feature{position:relative;height:100%;padding:18px 26px}
.feature + .feature{border-left:2px solid var(--divider)}
.feature:nth-child(1){width:376px}
.feature:nth-child(2){width:375px}
.feature:nth-child(3){width:377px}
.feature h2{font-family:"Ubuntu",sans-serif;font-size:19px;font-weight:500;color:var(--orange);line-height:24px}
.feature p{font-size:14.4px;line-height:28.8px;margin-top:5px;color:var(--text)}
.feature ul li{position:relative;padding-left:24px;font-size:14.4px;line-height:28.8px}
.feature ul li::before{content:"";position:absolute;left:5px;top:10px;width:7px;height:7px;border-right:2px solid var(--text-dark);border-top:2px solid var(--text-dark);transform:rotate(45deg)}
.read-more{position:absolute;bottom:10px;right:14px;width:115px;height:34px;background:#fff;border-radius:17px;box-shadow:0 1px 3px rgba(0,0,0,.25);display:flex;align-items:center;justify-content:center;gap:8px;font-family:"Ubuntu",sans-serif;font-size:15px;font-weight:500;color:var(--orange)}
.read-more::after{content:"";width:6px;height:6px;border-right:2px solid var(--text-dark);border-top:2px solid var(--text-dark);transform:rotate(45deg)}
.feature-sub{font-weight:700;color:var(--text-dark);font-size:14.4px;margin-top:8px}
.overview{display:flex;gap:18px;margin-top:10px}
.overview-photo{flex:0 0 143px;height:91px;border:2px solid #fff;box-shadow:0 0 2px rgba(0,0,0,.4);background:linear-gradient(135deg,#52606c,#2b3540 60%,#8a949c)}
.overview p{margin-top:0;font-size:14.4px;line-height:20.4px;text-align:justify;padding-top:2px}

/* Footer */
.footer-cols{position:absolute;top:848px;left:0;width:1200px}
.footer-col{position:absolute;top:0}
.footer-col h3{font-family:"Arimo",sans-serif;font-size:15px;font-weight:700;color:var(--navy);line-height:20px}
.footer-col ul{margin-top:18px}
.footer-col li{font-size:14.4px;line-height:28.8px;color:var(--text)}
.footer-col .accent{color:var(--orange)}
.footer-col .accent-bold{color:var(--orange);font-weight:700}
.social{position:absolute;top:847px;left:1015px;display:flex;gap:12px}
.social span{width:34px;height:34px;border-radius:4px}
.social .feed{background:#f49a3a}
.social .network{background:#1b75b3}
.social .micro{background:#45b6ea}

.footer-rule{position:absolute;left:36px;top:1061px;width:1128px;height:3px;background:var(--rule)}
.bottom-bar{position:absolute;top:1087px;left:44px;width:1122px;display:flex;justify-content:space-between;font-size:16.8px;color:var(--text)}
.bottom-links{display:flex;gap:16px}
.copyright{font-size:16.5px}
</style>
</head>
<body>

<header>
  <a class="brand" href="#"><span class="brand-name">Ko-Brava</span></a>
  <div class="utility">
    <nav class="utility-links">
      <a href="#">BLOG</a><span class="sep">|</span>
      <a href="#">FAQ</a><span class="sep">|</span>
      <a href="#">CONTACT</a>
    </nav>
    <div class="search">
      <span>Search...</span>
      <svg width="14" height="16" viewBox="0 0 14 16"><path d="M3 2 L10 8 L3 14" fill="none" stroke="#ff6c00" stroke-width="3"/></svg>
    </div>
  </div>
</header>

<main class="panel">
  <nav class="nav">
    <a href="#" class="is-active" style="width:180px">HOME</a>
    <a href="#" style="width:190px">ABOUT US</a>
    <a href="#" style="width:194px">SERVICES</a>
    <a href="#" style="width:199px">PARTNERS</a>
    <a href="#" style="width:177px">CAPABILITIES</a>
    <a href="#" style="width:188px">CAREERS</a>
  </nav>

  <section class="hero" role="img" aria-label="Photo of a city skyline with construction cranes and a steel-frame building under construction by the water">
    <div class="hero-caption">
      <h1 class="hero-title">Vancouver BC- Based Technology Infrastructure Specialists</h1>
      <p class="hero-text">With over 100 years of collective technology and operations experience under our belt, the Ko-Brava team can deliver the option that your company needs to drive you into the future.</p>
    </div>
    <div class="slider-dots">
      <span class="is-current"></span><span></span><span></span><span></span>
    </div>
  </section>

  <section class="features">
    <article class="feature">
      <h2>Core Capabilities</h2>
      <p style="text-align:justify">Ko-Brava is a leader in Technology Infrastructue Engineering and Project Management.</p>
      <ul>
        <li>Project Management</li>
        <li>IBT</li>
        <li>SMB Support</li>
        <li>Virtualization</li>
      </ul>
      <a class="read-more" href="#">Read More</a>
    </article>
    <article class="feature">
      <h2>WHY CHOOSE US?</h2>
      <p>Proven results, Proven Staff</p>
      <ul>
        <li>VERD AP Staff Members</li>
        <li>ITSL Certified Staff Members</li>
        <li>CNIE Certified Staff Members</li>
        <li>PMX Certified Staff Members</li>
      </ul>
      <a class="read-more" href="#">Read More</a>
    </article>
    <article class="feature">
      <h2>SERVICES OVERVIEW</h2>
      <div class="feature-sub">Technology Project Management</div>
      <div class="overview">
        <div class="overview-photo" role="img" aria-label="Photo of a business team meeting around a table"></div>
        <p>We can make sense of the most challenging intergration projects or design...</p>
      </div>
      <a class="read-more" href="#">Read More</a>
    </article>
  </section>
</main>

<footer>
  <div class="footer-cols">
    <div class="footer-col" style="left:56px">
      <h3>Company</h3>
      <ul><li>About Us</li><li>News &amp; Events</li><li>Work</li><li>FAQ`s</li><li>Contacts</li></ul>
    </div>
    <div class="footer-col" style="left:221px">
      <h3>Services</h3>
      <ul><li>IT Project Management</li><li>VIOP Implementation</li><li>Virtualization</li><li>LAN / WAN Connectivity</li><li>IBT</li></ul>
    </div>
    <div class="footer-col" style="left:426px">
      <h3>Partners</h3>
      <ul><li>Directory</li><li>Partner Program</li><li>How to become a Partner</li><li>How to Find them</li><li>Key Partners</li></ul>
    </div>
    <div class="footer-col" style="left:629px">
      <h3>Careers</h3>
      <ul><li>Training</li><li>Support / Notice</li><li>Professional Services</li><li>Certificates</li><li>Interview Process</li></ul>
    </div>
    <div class="footer-col" style="left:820px">
      <h3>Corporate Links</h3>
      <ul><li>Ko-Brava <span class="accent">FTP SITE</span></li><li>Web Timesheets</li><li>Ko-Brava for Clients</li><li>Jobs Site Photos</li><li class="accent-bold">Free FTP Client Software</li></ul>
    </div>
  </div>
  <div class="social" aria-label="Social links">
    <span class="feed"></span><span class="network"></span><span class="micro"></span>
  </div>
  <div class="footer-rule"></div>
  <div class="bottom-bar">
    <nav class="bottom-links">
      <a href="#">Home</a><span>|</span><a href="#">Contacts</a><span>|</span><a href="#">News</a><span>|</span><a href="#">Policy</a>
    </nav>
    <span class="copyright">Ko-Brava Technology Solutions © 2011. All rights reserved.</span>
  </div>
</footer>

</body>
</html>
```